Floral Design for Weddings And Events

I create floral designs for weddings and events. I create unusual designs that people will remember.

Industry/Entity Type

Floral

Contact Information for Business Card

Reeds
Weddings and Events
Marlene Dukov, owner/designer
2817 Corvell Ln
Eldridge Falls, OR 97341
marlyduknv@mailbrook.net
412 736-2185

Requirements
Must have
• I would like the name of the business, REEDS, to Stand Out!! I like clean, bold lines.. nothing foo-foo! Must be easy to read I'm looking for a design that catches your eye and represents my creativity. I want my card to show the potential customer that I'm unique and creative
Nice to have
• I'm thinking of the name REEDS maybe worked into the design... I'm open to your creative ideas!!!! The name must be very legible
Should not have
• I'm open to any colors other that pink and yellow..nothing Foo-Foo or flowery..

```html
<!DOCTYPE html>
<html lang="en">
<head>
<meta charset="utf-8">
<title>Reeds — Weddings and Events business card</title>
<link href="https://fonts.googleapis.com/css2?family=Jost:wght@300;400;600&display=swap" rel="stylesheet">
<style>
  :root {
    --page: #e6e6e4;
    --mint: #b1dad1;
    --paper: #ffffff;
    --gold: #a8772f;
    --gold-soft: #c69a57;
    --shadow: rgba(0,0,0,0.18);
  }
  * { margin: 0; padding: 0; box-sizing: border-box; }
  html, body { width: 1200px; height: 720px; overflow: hidden; }
  body {
    background: var(--page);
    font-family: "Jost", "Century Gothic", sans-serif;
    color: var(--gold);
    position: relative;
  }
  .card {
    position: absolute;
    top: 211px;
    width: 520px;
    height: 297px;
    box-shadow: 0 6px 18px var(--shadow);
    overflow: hidden;
  }
  .card--front { left: 50px; background: var(--mint); }
  .card--back { left: 630px; background: var(--paper); }

  .ornament {
    position: absolute;
    border-radius: 14px;
    background: linear-gradient(90deg, rgba(168,119,47,0.15), var(--gold-soft) 30%, var(--gold) 50%, var(--gold-soft) 70%, rgba(168,119,47,0.15));
  }
  .rule { position: absolute; height: 1.5px; background: var(--gold); }

  .wordmark {
    position: absolute;
    left: 0; right: 0;
    text-align: center;
    font-weight: 300;
    line-height: 1;
    letter-spacing: 1px;
  }
  .tagline {
    position: absolute;
    left: 0; right: 0;
    text-align: center;
    font-weight: 300;
    letter-spacing: 0.5px;
  }

  /* front */
  .card--front .ornament--top { left: 140px; top: 34px; width: 240px; height: 26px; }
  .card--front .rule--top { left: 95px; width: 330px; top: 72px; }
  .card--front .wordmark { top: 80px; font-size: 88px; }
  .card--front .tagline { top: 176px; font-size: 22px; }
  .card--front .rule--bottom { left: 95px; width: 330px; top: 212px; }
  .card--front .ornament--bottom { left: 125px; top: 226px; width: 270px; height: 38px; }

  /* back: logo block */
  .logo-block { position: absolute; left: 26px; top: 22px; width: 230px; height: 170px; }
  .logo-block .ornament--top { left: 45px; top: 0; width: 140px; height: 18px; }
  .logo-block .rule--top { left: 15px; width: 200px; top: 28px; }
  .logo-block .wordmark { top: 34px; font-size: 52px; }
  .logo-block .tagline { top: 92px; font-size: 14px; }
  .logo-block .rule--bottom { left: 15px; width: 200px; top: 118px; }
  .logo-block .ornament--bottom { left: 35px; top: 128px; width: 160px; height: 24px; }

  .address {
    position: absolute;
    left: 34px; top: 212px;
    font-size: 15px;
    line-height: 1.45;
    font-weight: 600;
    font-style: normal;
  }

  .contact {
    position: absolute;
    right: 30px; bottom: 26px;
    text-align: right;
  }
  .contact__name { font-size: 22px; font-weight: 600; letter-spacing: 0.3px; line-height: 1.2; }
  .contact__role { font-size: 15px; font-weight: 400; margin-bottom: 10px; }
  .contact__line {
    font-size: 14px;
    font-weight: 400;
    display: flex;
    justify-content: flex-end;
    align-items: center;
    gap: 7px;
    line-height: 1.6;
  }
  .contact__line svg { width: 13px; height: 13px; flex: none; }
</style>
</head>
<body>
  <section class="card card--front" aria-label="Card front">
    <div class="ornament ornament--top" role="img" aria-label="Gold filigree scroll ornament"></div>
    <div class="rule rule--top"></div>
    <h1 class="wordmark">Reeds</h1>
    <p class="tagline">Weddings and Events</p>
    <div class="rule rule--bottom"></div>
    <div class="ornament ornament--bottom" role="img" aria-label="Gold filigree scroll ornament"></div>
  </section>

  <section class="card card--back" aria-label="Card back">
    <div class="logo-block">
      <div class="ornament ornament--top" role="img" aria-label="Gold filigree scroll ornament"></div>
      <div class="rule rule--top"></div>
      <p class="wordmark">Reeds</p>
      <p class="tagline">Weddings and Events</p>
      <div class="rule rule--bottom"></div>
      <div class="ornament ornament--bottom" role="img" aria-label="Gold filigree scroll ornament"></div>
    </div>

    <address class="address">
      2817 Corvell Ln Eldridge Falls,<br>OR 97341
    </address>

    <div class="contact">
      <p class="contact__name">Marlene Dukov</p>
      <p class="contact__role">owner / designer</p>
      <p class="contact__line">412 736-2185
        <svg viewBox="0 0 12 12" aria-hidden="true"><rect x="3" y="0.5" width="6" height="11" rx="1" fill="none" stroke="currentColor"/><rect x="4.2" y="2" width="3.6" height="5" fill="currentColor"/></svg>
      </p>
      <p class="contact__line">marlyduknv@mailbrook.net
        <svg viewBox="0 0 12 12" aria-hidden="true"><rect x="0.5" y="2.5" width="11" height="7" fill="none" stroke="currentColor"/><path d="M0.5 2.5 L6 6.5 L11.5 2.5 M0.5 9.5 L4.5 5.5 M11.5 9.5 L7.5 5.5" fill="none" stroke="currentColor"/></svg>
      </p>
    </div>
  </section>
</body>
</html>
```